Existing Website Requiring new Pages

I have an existing word press website that was built using elementor.
Website: www.tallowmerecare.com.au
I require the Vacancies page (https://www.tallowmerecare.com.au/vacancies/) to be modified to display our new properties along with minor tweaks to how the information is presented.
The vacancies to be displayed are the exactly the same as those that are located on the homepage of QDA website (https://qda.org.au/)
The new pages that link off the Vacancies tab will require custom design.
There are roughly 8 pages/properties to be incorporated. i wish for the design to be very similar to that displayed in the following link; https://www.zomplex.com.au/vacancies/merrylands
Along with this the back end has not been updated for the last 3 years so it also requires some maintenance.
Website is in the disability industry and the custom pages will display information relative to Property Vacancies.
I have attached a ZIP file with some design guides, the information for each of the properties (which will need to be modified to show our business name Tallowmere Healthcare) and the example of how it is to look based off the Zomplex website.
If you guys have any suggestions or ideas on how to make this more presentable or possible i'm open to your ideas.
People looking for SDA properties custom built for people with a disability
Disability
Coded - Design and coding required
5+ page

```html
<!DOCTYPE html>
<html lang="en">
<head>
<meta charset="utf-8">
<title>Vacancies | Tallowmere Healthcare</title>
<link href="https://fonts.googleapis.com/css2?family=Montserrat:wght@400;500;600;700;800&family=Roboto:wght@400;500&display=swap" rel="stylesheet">
<style>
:root{
  --purple:#8462d4;
  --purple-light:#9373dc;
  --ink:#24232f;
  --muted:#6f6f7a;
  --orange:#f2712d;
  --pink:#e8448c;
  --line:#e6e6ec;
  --footer-bg:#f7f7f9;
  --bar:#1f1f24;
  --tag:#4a4a55;
  --green:#2ec48a;
}
*{box-sizing:border-box;margin:0;padding:0}
html,body{width:1200px;height:3460px;overflow:hidden;background:#fff;font-family:"Roboto",sans-serif;color:var(--ink)}
.page{position:relative;width:1200px;height:3460px;overflow:hidden}
.abs{position:absolute}

/* header */
.brand{position:absolute;left:62px;top:40px;display:flex;align-items:center;gap:10px}
.brand-dot{width:26px;height:26px;border-radius:50%;background:var(--pink)}
.brand-name{font-family:"Montserrat",sans-serif;font-weight:700;font-size:24px;color:var(--purple);line-height:1}
.nav{position:absolute;right:48px;top:63px;display:flex;gap:27px;font-family:"Montserrat",sans-serif;font-weight:700;font-size:11.5px;letter-spacing:.6px;color:#3a3a46}
.nav .active{color:var(--orange)}

/* hero */
.hero{position:absolute;left:0;top:148px;width:1200px;height:535px;background:var(--purple);overflow:hidden}
.hero-eyebrow{position:absolute;left:84px;top:196px;font-family:"Montserrat",sans-serif;font-weight:700;font-size:30px;color:#fff}
.hero-title{position:absolute;left:82px;top:228px;font-family:"Montserrat",sans-serif;font-weight:800;font-size:88px;color:#fff;letter-spacing:-1px}
.hero-photo{position:absolute;left:607px;top:212px;width:497px;height:583px;border-radius:12px;background:linear-gradient(160deg,#7c7b78 0%,#5f5e5a 45%,#c99a4a 60%,#4b4a46 100%);box-shadow:0 18px 40px rgba(0,0,0,.15)}
.arrow{position:absolute;top:660px;width:46px;height:46px;border-radius:50%;background:rgba(255,255,255,.18);display:flex;align-items:center;justify-content:center}
.search{position:absolute;left:86px;top:627px;width:707px;height:109px;background:#fff;border-radius:6px;box-shadow:0 10px 30px rgba(40,30,80,.12)}
.field{position:absolute;top:22px;width:173px}
.field label{display:block;font-family:"Montserrat",sans-serif;font-weight:700;font-size:10px;color:#2a2a33;margin-bottom:9px;letter-spacing:.2px}
.select{height:40px;border-radius:4px;background:#f1f1f4;padding:0 14px;display:flex;align-items:center;justify-content:space-between;font-size:12px;color:#6a6a73}
.go{position:absolute;left:608px;top:43px;width:74px;height:41px;background:var(--pink);border-radius:4px;color:#fff;font-family:"Montserrat",sans-serif;font-weight:700;font-size:20px;display:flex;align-items:center;justify-content:center}

/* sections */
.eyebrow{position:absolute;left:114px;font-family:"Montserrat",sans-serif;font-weight:600;font-size:12px;color:var(--orange);letter-spacing:.5px}
.section-title{position:absolute;left:114px;font-family:"Montserrat",sans-serif;font-weight:700;font-size:30px;color:var(--ink)}
.map{position:absolute;left:122px;top:974px;width:956px;height:440px;border-radius:14px;background:linear-gradient(90deg,#cfe3c9 0%,#e8efe6 45%,#f1f1ee 62%,#a9d6ec 70%,#92cfe8 100%);box-shadow:0 20px 40px rgba(0,0,0,.08)}

/* cards */
.card{position:absolute;width:304px;height:423px;background:#fff;border-radius:4px;box-shadow:0 6px 24px rgba(30,30,60,.09);overflow:hidden}
.card-img{position:absolute;left:0;top:0;width:304px;height:236px}
.tags{position:absolute;top:14px;left:14px;right:14px;display:flex;gap:6px}
.tag{height:15px;padding:0 7px;background:var(--tag);color:#fff;font-family:"Montserrat",sans-serif;font-weight:700;font-size:7px;display:flex;align-items:center;border-radius:2px}
.tag.feat{background:var(--green);margin-right:auto}
.tags.right{justify-content:flex-end}
.dots{position:absolute;top:214px;left:134px;display:flex;gap:7px}
.dots i{width:5px;height:5px;border-radius:50%;background:rgba(255,255,255,.55)}
.dots i.on{background:#fff}
.expand{position:absolute;right:14px;top:196px;width:24px;height:24px;background:rgba(0,0,0,.55);border-radius:3px}
.card h3{position:absolute;left:26px;top:255px;font-family:"Montserrat",sans-serif;font-weight:700;font-size:17px;color:var(--ink)}
.loc{position:absolute;left:26px;top:281px;font-size:12px;color:var(--muted);display:flex;align-items:center;gap:5px}
.card hr{position:absolute;left:26px;right:26px;top:305px;border:0;border-top:1px solid var(--line)}
.feat-list{position:absolute;left:26px;top:320px;list-style:none;font-size:12px;color:#55555f;line-height:20px}
.feat-list li:before{content:"";display:inline-block;width:4px;height:4px;border-radius:50%;background:#bbb;margin-right:9px;vertical-align:middle}
.details{position:absolute;left:28px;top:369px;height:28px;padding:0 12px;background:var(--orange);color:#fff;font-family:"Montserrat",sans-serif;font-weight:700;font-size:12px;border-radius:4px;display:flex;align-items:center}

/* footer */
.footer{position:absolute;left:0;top:3068px;width:1200px;height:320px;background:var(--footer-bg)}
.footer .brand{left:75px;top:108px}
.contact{position:absolute;left:73px;top:225px;font-size:13.5px;color:var(--muted);line-height:24px}
.contact div{display:flex;align-items:center;gap:8px}
.social{position:absolute;left:515px;width:33px;height:33px;border-radius:50%}
.fcol{position:absolute;top:70px;width:242px}
.fcol h4{font-family:"Montserrat",sans-serif;font-weight:500;font-size:15px;color:#2a2a35;border-left:3px solid #3b6fd6;padding-left:14px;margin-bottom:22px;letter-spacing:.4px}
.fcol a{display:block;font-size:13.5px;color:#8a8a94;line-height:22px;padding:6px 0 7px;border-bottom:1px solid var(--line);text-decoration:none}
.bottom-bar{position:absolute;left:0;top:3388px;width:1200px;height:72px;background:var(--bar);color:#b9b9c2;font-size:11px;display:flex;align-items:center;justify-content:center}
</style>
</head>
<body>
<div class="page">

<header>
  <div class="brand"><span class="brand-dot"></span><span class="brand-name">Tallowmere</span></div>
  <nav class="nav">
    <span>HOME</span><span>ABOUT US</span><span class="active">WHAT WE DO ⌄</span><span>REFERRALS</span><span>FEEDBACK</span><span>CONTACT US</span>
  </nav>
</header>

<section class="hero">
  <svg class="abs" style="left:0;top:0" width="1200" height="535"><path d="M0 0 H260 C420 200 620 300 640 535 H0 Z" fill="var(--purple-light)" opacity=".55"/></svg>
  <div class="hero-eyebrow">Tallowmere Healthcare</div>
  <div class="hero-title">Vacancies</div>
</section>
<div class="hero-photo" role="img" aria-label="Woman in a wheelchair working on a laptop at a kitchen bench"></div>
<div class="arrow" style="left:961px"><svg width="12" height="12"><path d="M8 2 L4 6 L8 10" stroke="#fff" stroke-width="1.8" fill="none"/></svg></div>
<div class="arrow" style="left:1017px"><svg width="12" height="12"><path d="M4 2 L8 6 L4 10" stroke="#fff" stroke-width="1.8" fill="none"/></svg></div>

<form class="search">
  <div class="field" style="left:39px"><label>CURRENT OF FUTURE</label><div class="select">Both <span>⇕</span></div></div>
  <div class="field" style="left:224px"><label>DESIGN CATEGORY</label><div class="select">All Category <span>⇕</span></div></div>
  <div class="field" style="left:409px"><label>LOCATION</label><div class="select">All Suburbs <span>⇕</span></div></div>
  <div class="go">GO</div>
</form>

<div class="eyebrow" style="top:872px">LOCATIONS</div>
<h2 class="section-title" style="top:895px">View Our SDA Vacancies and Homes Being Built</h2>
<div class="map" role="img" aria-label="Map of Greater Western Sydney showing property locations"></div>

<div class="eyebrow" style="top:1517px">PROPERTIES</div>
<h2 class="section-title" style="top:1541px">Properties List View</h2>

<!-- row 1 -->
<article class="card" style="left:114px;top:1621px">
  <div class="card-img" role="img" aria-label="Brick townhouse exterior" style="background:linear-gradient(180deg,#7fa6cf 0%,#9a8a70 45%,#6f6458 100%)"></div>
  <div class="tags"><span class="tag feat">FEATURED</span><span class="tag">ALMOST FULL - APPLY NOW!</span><span class="tag">APPLY NOW!</span></div>
  <div class="dots"><i></i><i class="on"></i><i></i></div><div class="expand"></div>
  <h3>SDA in Greystanes</h3>
  <div class="loc"><svg width="9" height="12"><path d="M4.5 0C2 0 0 2 0 4.5 0 8 4.5 12 4.5 12S9 8 9 4.5C9 2 7 0 4.5 0Z" fill="#bbb"/></svg>Greystanes</div>
  <hr><ul class="feat-list"><li>Fully Accessible</li><li>High Physical Support</li></ul>
  <div class="details">Details</div>
</article>
<article class="card" style="left:448px;top:1621px">
  <div class="card-img" role="img" aria-label="Two-storey house with garage" style="background:linear-gradient(180deg,#9fb3c9 0%,#8e8d8a 50%,#55524f 100%)"></div>
  <div class="tags"><span class="tag feat">FEATURED</span><span class="tag">AVAILABLE NOW</span><span class="tag">CURRENT VACANCY</span></div>
  <div class="dots"><i></i><i class="on"></i><i></i></div><div class="expand"></div>
  <h3>SDA in Jordan Springs</h3>
  <div class="loc"><svg width="9" height="12"><path d="M4.5 0C2 0 0 2 0 4.5 0 8 4.5 12 4.5 12S9 8 9 4.5C9 2 7 0 4.5 0Z" fill="#bbb"/></svg>Jordan Springs</div>
  <hr><ul class="feat-list"><li>Fully Accessible</li><li>Improved Liveability</li></ul>
  <div class="details">Details</div>
</article>
<article class="card" style="left:782px;top:1621px">
  <div class="card-img" role="img" aria-label="Row of modern townhouses" style="background:linear-gradient(180deg,#b9c2cc 0%,#8f8b85 50%,#4f5a4c 100%)"></div>
  <div class="tags"><span class="tag feat">FEATURED</span><span class="tag">AVAILABLE NOW</span><span class="tag">CURRENT VACANCY</span></div>
  <div class="dots"><i></i><i class="on"></i><i></i></div><div class="expand"></div>
  <h3>SDA in Werrington</h3>
  <div class="loc"><svg width="9" height="12"><path d="M4.5 0C2 0 0 2 0 4.5 0 8 4.5 12 4.5 12S9 8 9 4.5C9 2 7 0 4.5 0Z" fill="#bbb"/></svg>Werrington</div>
  <hr><ul class="feat-list"><li>Fully Accessible</li><li>Improved Liveability</li></ul>
  <div class="details">Details</div>
</article>

<!-- row 2 -->
<article class="card" style="left:114px;top:2079px">
  <div class="card-img" role="img" aria-label="Single-storey villas with white doors" style="background:linear-gradient(180deg,#8fb2d8 0%,#5d6468 55%,#3f4446 100%)"></div>
  <div class="tags"><span class="tag feat">FEATURED</span><span class="tag">AVAILABLE NOW</span><span class="tag">NEW CONSTRUCTION</span></div>
  <div class="dots"><i></i><i class="on"></i><i></i></div><div class="expand"></div>
  <h3>SDA villas in Wentworthville</h3>
  <div class="loc"><svg width="9" height="12"><path d="M4.5 0C2 0 0 2 0 4.5 0 8 4.5 12 4.5 12S9 8 9 4.5C9 2 7 0 4.5 0Z" fill="#bbb"/></svg>Wentworthville</div>
  <hr><ul class="feat-list"><li>Fully Accessible</li><li>High Physical Support</li></ul>
  <div class="details">Details</div>
</article>
<article class="card" style="left:448px;top:2079px">
  <div class="card-img" role="img" aria-label="Brick duplex with balconies" style="background:linear-gradient(180deg,#6f97cf 0%,#7a6e66 50%,#3d3d40 100%)"></div>
  <div class="tags right"><span class="tag">CURRENT VACANCY</span><span class="tag">APPLY NOW</span></div>
  <div class="dots"><i></i><i class="on"></i><i></i></div><div class="expand"></div>
  <h3>SDA in West Pennant Hills</h3>
  <div class="loc"><svg width="9" height="12"><path d="M4.5 0C2 0 0 2 0 4.5 0 8 4.5 12 4.5 12S9 8 9 4.5C9 2 7 0 4.5 0Z" fill="#bbb"/></svg>West Pennant Hills</div>
  <hr><ul class="feat-list"><li>High Physical Support</li><li>Improved Liveability</li></ul>
  <div class="details">Details</div>
</article>
<article class="card" style="left:782px;top:2079px">
  <div class="card-img" role="img" aria-label="Two-storey brick home under construction" style="background:linear-gradient(180deg,#6b95d2 0%,#8a7f77 50%,#4a4644 100%)"></div>
  <div class="tags right"><span class="tag">NEW CONSTRUCTION</span><span class="tag">APPLY NOW</span></div>
  <div class="dots"><i></i><i class="on"></i><i></i></div><div class="expand"></div>
  <h3>SDA in Guildford West</h3>
  <div class="loc"><svg width="9" height="12"><path d="M4.5 0C2 0 0 2 0 4.5 0 8 4.5 12 4.5 12S9 8 9 4.5C9 2 7 0 4.5 0Z" fill="#bbb"/></svg>Guildford West</div>
  <hr><ul class="feat-list"><li>Fully Accessible</li><li>High Physical Support</li></ul>
  <div class="details">Details</div>
</article>

<!-- row 3 -->
<article class="card" style="left:114px;top:2537px">
  <div class="card-img" role="img" aria-label="Rendered home with landscaped front garden" style="background:linear-gradient(180deg,#a8c4e2 0%,#a99382 50%,#5e7a4a 100%)"></div>
  <div class="tags right"><span class="tag">REGISTER YOUR INTEREST TODAY</span><span class="tag">APPLY NOW</span></div>
  <div class="dots"><i></i><i class="on"></i><i></i></div><div class="expand"></div>
  <h3>SDA in Austral</h3>
  <div class="loc"><svg width="9" height="12"><path d="M4.5 0C2 0 0 2 0 4.5 0 8 4.5 12 4.5 12S9 8 9 4.5C9 2 7 0 4.5 0Z" fill="#bbb"/></svg>Austral</div>
  <hr><ul class="feat-list"><li>Fully Accessible</li><li>High Physical Support</li></ul>
  <div class="details">Details</div>
</article>
<article class="card" style="left:448px;top:2537px">
  <div class="card-img" role="img" aria-label="Brick townhouses along a street" style="background:linear-gradient(180deg,#7ea3d6 0%,#92705a 50%,#54504c 100%)"></div>
  <div class="tags right"><span class="tag">AVAILABLE NOW</span><span class="tag">CURRENT VACANCY</span></div>
  <div class="dots"><i></i><i class="on"></i><i></i></div><div class="expand"></div>
  <h3>SDA in Merrylands</h3>
  <div class="loc"><svg width="9" height="12"><path d="M4.5 0C2 0 0 2 0 4.5 0 8 4.5 12 4.5 12S9 8 9 4.5C9 2 7 0 4.5 0Z" fill="#bbb"/></svg>Merrylands</div>
  <hr><ul class="feat-list"><li>Fully Accessible Disability</li><li>High Physical Support</li></ul>
  <div class="details">Details</div>
</article>
<article class="card" style="left:782px;top:2537px">
  <div class="card-img" role="img" aria-label="Dark brick home with white garage door" style="background:linear-gradient(180deg,#c6ccd4 0%,#6b6b70 50%,#3a3a3e 100%)"></div>
  <div class="tags right"><span class="tag">EXPRESSION OF INTEREST</span><span class="tag">APPLY NOW</span></div>
  <div class="dots"><i></i><i class="on"></i><i></i></div><div class="expand"></div>
  <h3>SDA in Blacktown..</h3>
  <div class="loc"><svg width="9" height="12"><path d="M4.5 0C2 0 0 2 0 4.5 0 8 4.5 12 4.5 12S9 8 9 4.5C9 2 7 0 4.5 0Z" fill="#bbb"/></svg>Blacktown</div>
  <hr><ul class="feat-list"><li>Fully Accessible</li><li>High Physical Support</li></ul>
  <div class="details">Details</div>
</article>

<footer class="footer">
  <div class="brand"><span class="brand-dot"></span><span class="brand-name">Tallowmere</span></div>
  <div class="contact">
    <div><svg width="13" height="11"><rect x=".5" y=".5" width="12" height="10" fill="none" stroke="var(--pink)"/><path d="M.5 .5 L6.5 6 L12.5 .5" fill="none" stroke="var(--pink)"/></svg>Email: info@tallowmerecare.com.au</div>
    <div><svg width="13" height="13"><path d="M2 1 L5 1 L6 4 L4 5.5 C5 8 6 9 8.5 10 L10 8 L13 9 L13 12 C6 13 0 7 1 1Z" fill="var(--pink)"/></svg>Phone: +61 0412 555 308</div>
    <div><svg width="13" height="13"><circle cx="6.5" cy="6.5" r="5.5" fill="none" stroke="var(--pink)" stroke-width="1.4"/><path d="M6.5 3.5 V6.5 L8.5 8" stroke="var(--pink)" stroke-width="1.4" fill="none"/></svg>Operating Hours: 9AM To 5PM Monday - Friday</div>
  </div>
  <div class="social" style="top:70px;background:#6a3fa0"></div>
  <div class="social" style="top:115px;background:#2f4f9c"></div>
  <div class="social" style="top:160px;background:#222"></div>
  <div class="social" style="top:205px;background:#1f7bbf"></div>
  <div class="fcol" style="left:613px">
    <h4>ACCOMMODATION</h4>
    <a>Supported Independent Living (SIL)</a>
    <a>Specialist Disability Accommodation (SDA)</a>
    <a>Short term Accommodation (Respite)</a>
    <a>Vacancies</a>
  </div>
  <div class="fcol" style="left:883px">
    <h4>WHAT WE DO</h4>
    <a>In Home Care</a>
    <a>Social &amp; Community Services</a>
    <a>Therapeutic Supports</a>
    <a>Support Coordination</a>
    <a>Home Modifications</a>
  </div>
</footer>
<div class="bottom-bar">© Copyright 2021 | Tallowmere Healthcare | All Rights Reserved.</div>

</div>
</body>
</html>
```